Kestrel Plumbing business card full re design & logo design

Kestrel Plumbing is a Sydney based mechanical plumbing contractor company.
We would like a full redesign with new logo etc which we can take to a future website, uniforms, vehicle sign writing etc.
Blue is my preferred choice of colour but i would be open to see a couple of alternatives thrown in the mix to see how they compare. I am open to see on white cards, black cards etc. Open to many new ideas.
Please see attached original business cards which have been used for the last 5 years.

Target Market(s)

Mechanical services industry.

Industry/Entity Type

Plumbing

Contact Information for Business Card

Dale Fenmore
Director

Mob: 0427 596 418
Email: dale@kestrelplumbing-demo.net.au
PO BOX 782
Marrick Vale NSW 2158
Lic: 518604k

Logo Text

Kestrel Plumbing

Font styles to use
Sans Serif

Colors
0655a3
3276b5
0792cd
33a6d7
85cae6
000000
333333
474747

Requirements
Must have
• Things that make it very professional and very well presented.
Nice to have
• Same description or very similar to attached uploaded file
Should not have
• Anything that makes it look unprofessional or cartoony.

```html
<!DOCTYPE html>
<html lang="en">
<head>
<meta charset="utf-8">
<title>Kestrel Plumbing – Business Card</title>
<link href="https://fonts.googleapis.com/css2?family=Lato:wght@400;700;900&display=swap" rel="stylesheet">
<style>
  :root {
    --backdrop: #3a3634;
    --card-black: #0d0d0d;
    --card-blue: #1a6396;
    --brand-blue: #0792cd;
    --name-blue: #3276b5;
    --text-light: #e8e8e8;
    --rule-dark: #474747;
    --rule-light: rgba(255,255,255,0.55);
  }
  * { margin: 0; padding: 0; box-sizing: border-box; }
  html, body { width: 1200px; height: 900px; overflow: hidden; }
  body {
    background: var(--backdrop);
    font-family: "Lato", sans-serif;
    position: relative;
  }
  .card {
    position: absolute;
    width: 525px;
    height: 300px;
    top: 300px;
    overflow: hidden;
    box-shadow: 0 12px 30px rgba(0,0,0,0.45);
  }
  .card--front { left: 50px; background: var(--card-black); }
  .card--back { left: 625px; background: var(--card-blue); }

  .front-brand {
    position: absolute;
    left: 0; top: 0;
    width: 265px; height: 100%;
    display: flex; align-items: center; justify-content: center;
    gap: 12px;
  }
  .brand-dot {
    width: 22px; height: 22px; border-radius: 50%;
    background: var(--brand-blue);
    flex: none;
  }
  .brand-name {
    font-weight: 900;
    font-size: 26px;
    letter-spacing: 1px;
    text-transform: uppercase;
    color: var(--brand-blue);
    line-height: 1.05;
  }
  .front-divider {
    position: absolute;
    left: 268px; top: 60px;
    width: 1px; height: 180px;
    background: var(--rule-dark);
  }
  .contact {
    position: absolute;
    left: 286px; top: 72px;
    right: 14px;
    color: var(--text-light);
    font-size: 13px;
    line-height: 1.4;
  }
  .contact__name {
    color: var(--name-blue);
    font-size: 18px;
    font-weight: 700;
    text-transform: uppercase;
    letter-spacing: 0.5px;
    line-height: 1.2;
  }
  .contact__role { margin-bottom: 6px; }
  .contact__line {
    display: flex; align-items: center; gap: 6px;
    font-size: 12.5px; white-space: nowrap;
  }
  .contact__line svg { width: 11px; height: 11px; fill: var(--brand-blue); flex: none; }
  .contact__address { margin-top: 10px; }

  .back-brand {
    position: absolute;
    left: 0; right: 0; top: 95px;
    display: flex; justify-content: center; align-items: center; gap: 14px;
  }
  .back-brand .brand-dot { background: #fff; width: 26px; height: 26px; }
  .back-brand .brand-name { color: #fff; font-size: 34px; }
  .back-rule {
    position: absolute;
    left: 130px; right: 130px; top: 195px;
    height: 1px; background: var(--rule-light);
  }
  .licence {
    position: absolute;
    left: 0; right: 0; top: 210px;
    text-align: center;
    color: #fff;
    font-size: 14px;
    letter-spacing: 0.5px;
  }
</style>
</head>
<body>
  <section class="card card--front">
    <div class="front-brand">
      <span class="brand-dot"></span>
      <span class="brand-name">Kestrel<br>Plumbing</span>
    </div>
    <div class="front-divider"></div>
    <div class="contact">
      <p class="contact__name">Dale Fenmore</p>
      <p class="contact__role">Director</p>
      <p class="contact__line">
        <svg viewBox="0 0 24 24" aria-hidden="true"><path d="M6.6 10.8a15 15 0 006.6 6.6l2.2-2.2a1 1 0 011-.25 11.4 11.4 0 003.6.57 1 1 0 011 1V20a1 1 0 01-1 1A17 17 0 013 4a1 1 0 011-1h3.5a1 1 0 011 1c0 1.25.2 2.45.57 3.57a1 1 0 01-.25 1z"/></svg>
        0427 596 418
      </p>
      <p class="contact__line">
        <svg viewBox="0 0 24 24" aria-hidden="true"><path d="M2 5h20v14H2z M2 5l10 8 10-8" /></svg>
        dale@kestrelplumbing-demo.net.au
      </p>
      <p class="contact__address">PO BOX 782 Marrick Vale<br>NSW 2158</p>
    </div>
  </section>

  <section class="card card--back">
    <div class="back-brand">
      <span class="brand-dot"></span>
      <span class="brand-name">Kestrel<br>Plumbing</span>
    </div>
    <div class="back-rule"></div>
    <p class="licence">LIC: 518604K</p>
  </section>
</body>
</html>
```